Innovative healthcare collaborative needs new look for business cards

CareLoomQ is a new kind of healthcare relationship company focused on aligning partners, innovation and solutions to provide needed health services to healthcare systems, hospitals or private business. Not mired in the old merger and acquisition fee-for-service framework, we focus on primary, secondary and tertiary service area partnership collaboratives. These networks are constructed by aligning healthcare services along a network of care, not just an individual patient care plan. This involves partnership arrangements with large or small medical centers, physician groups, allied health services, public health agencies, health insurers, et al as well as civic agencies, schools, farmers, supply chains to bring about needed healthcare solutions for patients. Think Green Havens. GH does for communities what we do for hospitals and health systems. We educate and instruct on strategic, operational, and innovative solutions for a healthcare provider, practice, business, or system resulting in successful construction of care networks (legal entity). We provide the blueprint of how to do this type of partnership, focused on what’s best for the sustainability of the business and the people (patients or potential patients) living there. Rural hospitals in particular are at risk.
We also provide seminars to academic, medical academic, and private industry to instruct on how to construct these care networks and educate on the essential criteria to be successful in the new healthcare era. We have been doing this work for the past 8 years, and since COVID-19, the recognition of fractured processes has boosted the demand. We need a business card that sets the tone that the traditional healthcare delivery system in the US has transformed (overnight). Our company is educating on how to transition current business models to the new world order in this space.
Brainstormed some business card tag lines for consideration:
CareLoomQ
• a healthcaring company
• allbettertogether
• Weaving care for every community

Target Market(s)

Health systems, hospitals, physician practices, academic medical schools, residency programs

Industry/Entity Type

Healthcare

Contact Information for Business Card

Doreen Vashtoll, Chief Relationship Officer
doreenvashtoll@mailpost-example.net
mobile: 415-286-9043

Font styles to use
Serif
Sans Serif

Requirements
Should not have
• Do not use word Consultant

```html
<!DOCTYPE html>
<html lang="en">
<head>
<meta charset="utf-8">
<title>CareLoomQ Business Card</title>
<link rel="stylesheet" href="https://fonts.googleapis.com/css2?family=Lato:ital,wght@0,400;0,700;0,900;1,400&display=swap">
<style>
  :root {
    --navy: #1b4173;
    --orange: #f07d2a;
    --paper: #f6f6f5;
    --ink: #1e1e22;
    --stage: #e4e5e8;
    --white: #ffffff;
  }
  * { box-sizing: border-box; margin: 0; padding: 0; }
  html, body { width: 1200px; height: 900px; overflow: hidden; }
  body {
    background: var(--stage);
    font-family: "Lato", sans-serif;
    display: flex;
    flex-direction: column;
    align-items: center;
    justify-content: center;
    gap: 36px;
  }
  .card {
    width: 700px;
    height: 400px;
    position: relative;
    box-shadow: 0 6px 18px rgba(0,0,0,0.18);
  }
  .card--front { background: var(--paper); }
  .card--back {
    background: var(--navy);
    display: flex;
    align-items: center;
    justify-content: center;
  }
  .brand { display: flex; flex-direction: column; align-items: flex-start; }
  .brand__name {
    font-weight: 900;
    letter-spacing: 1px;
    line-height: 1;
  }
  .brand__tagline {
    font-weight: 400;
    text-transform: uppercase;
    letter-spacing: 1.5px;
    margin-top: 6px;
  }
  .card--front .brand {
    position: absolute;
    left: 40px;
    top: 40px;
  }
  .card--front .brand__name { font-size: 60px; color: var(--navy); }
  .card--front .brand__tagline { font-size: 11px; color: var(--ink); }
  .card--back .brand__name { font-size: 84px; color: var(--white); }
  .card--back .brand__tagline { font-size: 15px; color: var(--white); }
  .person {
    position: absolute;
    right: 40px;
    top: 218px;
    text-align: right;
  }
  .person__name {
    font-weight: 700;
    font-size: 25px;
    line-height: 1.2;
    text-transform: uppercase;
    letter-spacing: 0.5px;
  }
  .person__first { color: var(--navy); }
  .person__last { color: var(--orange); }
  .person__title {
    font-size: 17px;
    color: var(--ink);
    margin-top: 2px;
  }
  .divider {
    position: absolute;
    left: 36px;
    right: 36px;
    top: 292px;
    height: 2px;
    background: var(--navy);
  }
  .contact {
    position: absolute;
    left: 40px;
    top: 310px;
    list-style: none;
    color: var(--ink);
  }
  .contact__item {
    display: flex;
    align-items: center;
    gap: 8px;
    margin-bottom: 4px;
  }
  .contact__phone { font-size: 22px; }
  .contact__email { font-size: 17px; }
  .contact__icon { width: 16px; height: 16px; flex: none; }
</style>
</head>
<body>
  <section class="card card--front">
    <div class="brand">
      <div class="brand__name">CareLoomQ</div>
      <div class="brand__tagline">Weaving care for every community</div>
    </div>
    <div class="person">
      <div class="person__name"><span class="person__first">Doreen</span> <span class="person__last">Vashtoll</span></div>
      <div class="person__title">Chief Relationship Officer</div>
    </div>
    <div class="divider"></div>
    <ul class="contact">
      <li class="contact__item contact__phone">
        <svg class="contact__icon" viewBox="0 0 16 16" aria-hidden="true">
          <rect x="4" y="1" width="8" height="14" rx="1.5" fill="none" stroke="#f07d2a" stroke-width="1.6"/>
          <circle cx="8" cy="12.3" r="0.9" fill="#f07d2a"/>
        </svg>
        415-286-9043
      </li>
      <li class="contact__item contact__email">
        <svg class="contact__icon" viewBox="0 0 16 16" aria-hidden="true">
          <rect x="1" y="3" width="14" height="10" fill="#f07d2a"/>
          <path d="M1 3 L8 9 L15 3" fill="none" stroke="#f6f6f5" stroke-width="1.3"/>
        </svg>
        doreenvashtoll@mailpost-example.net
      </li>
    </ul>
  </section>

  <section class="card card--back">
    <div class="brand">
      <div class="brand__name">CareLoomQ</div>
      <div class="brand__tagline">Weaving care for every community</div>
    </div>
  </section>
</body>
</html>
```